Clothing Brand E-Commerce Website Design

We would like you to provide an ecommerce design template in layered PSD for our clothing/fashion brand website called "TrelWick".
We want the site to have a simple but sleek design similar to the following sites:
http://www.pivorane.com/
http://corvatelle.com/
http://www.dulvenor.com/
We want it to look stunning and blow the example sites out of the water. For color scheme, please use your imagination and try to impress us with your creativity.
We like teal and beige pink, with teal dominant.
Teal #7AFFFF / #46C6C6
Beige/pink #FF7B7C / #C74646
We want you to develop the design for 3 pages:
1) Home Page
Samples:
http://www.pivorane.com/
http://corvatelle.com/
http://www.dulvenor.com/
2) Products List Page (e.g., lists all "Dresses" when category is selected)
http://www.pivorane.com/shop/casual-dresses
http://www.dulvenor.com/index.php?main_page=index&cPath=3
http://corvatelle.com/modest-dresses.html
http://www.quillmarsh.com/Product/Category.aspx?br=q47&category=dress_maxi
3) Product Detail Page (e.g., individual product page with "Add to Cart")
http://www.pivorane.com/shop/dresses/lumen-fern-dress
http://corvatelle.com/modest-dresses/modest-dress-tova.html
http://www.dulvenor.com/index.php?main_page=product_info&cPath=3&products_id=297
Industry/Entity Type
Fashion

```html
<!DOCTYPE html>
<html lang="en">
<head>
<meta charset="utf-8">
<title>TrelWick — Home</title>
<link href="https://fonts.googleapis.com/css2?family=Raleway:wght@400;500;600;700;800&family=Lato:ital,wght@0,400;0,700;1,400&display=swap" rel="stylesheet">
<style>
:root{
  --teal:#46c6c6;
  --teal-dark:#2f9ea0;
  --teal-hero:#8fd8d8;
  --pink:#ff7b7c;
  --pink-band:#ff8a8c;
  --red:#e0243a;
  --red-dark:#c74646;
  --ink:#444;
  --line:#e6e6e6;
  --soft:#f7f7f7;
  --white:#fff;
}
*{box-sizing:border-box;margin:0;padding:0}
html,body{width:1200px;height:2403px;overflow:hidden}
body{position:relative;background:var(--white);font-family:'Lato',sans-serif;color:var(--ink)}
.abs{position:absolute}

/* header */
.social-top{left:132px;top:22px;display:flex;gap:22px;font-size:11px;color:#d5d5d5}
.brand{left:0;width:1200px;top:24px;text-align:center;font-family:'Raleway',sans-serif;font-weight:700;font-size:22px;letter-spacing:1px;color:var(--teal)}
.user{right:176px;top:27px;font-size:11.5px;color:#555;white-space:nowrap}
.user b{font-weight:700;color:#333}
.cart{left:1034px;top:13px;width:34px;height:35px;background:#efefef}
.cart-count{left:1021px;top:4px;width:18px;height:18px;border-radius:50%;background:var(--pink);color:#fff;font-size:10px;text-align:center;line-height:18px}
.search{left:846px;top:48px;width:222px;height:33px;background:#eeeeee;border:1px solid #e2e2e2;font-size:12px;color:#aaa;padding:8px 8px}
.nav{left:0;width:1200px;top:100px;display:flex;justify-content:center;gap:6px;font-size:12.5px;color:#666}
.nav a{padding:5px 12px;color:inherit;text-decoration:none}
.nav a.active{background:var(--teal);color:#fff}
.nav-rule{left:0;top:145px;width:1200px;height:4px;border-top:1px solid #f3b8b9;border-bottom:1px solid #f3b8b9}
.nav-dot{top:141px;width:10px;height:10px;border-radius:50%;background:#fff;border:1px solid #f09a9b}

/* hero */
.hero{left:0;top:170px;width:1200px;height:368px;background:radial-gradient(ellipse at 45% 50%,#b9ecec 0%,var(--teal-hero) 55%,#7fcfcf 100%)}
.hero-title{left:239px;top:290px;font-family:'Raleway',sans-serif;font-weight:700;font-size:32px;letter-spacing:1.5px;color:#fff}
.hero-sub{left:239px;top:334px;font-family:'Raleway',sans-serif;font-size:17px;letter-spacing:5px;color:#eafafa}
.hero-btn{left:240px;top:383px;width:169px;height:40px;background:#fff;color:var(--teal-dark);font-family:'Raleway',sans-serif;font-weight:700;font-size:14px;letter-spacing:1px;text-align:center;line-height:40px}
.hero-photo{left:700px;top:170px;width:190px;height:368px;background:linear-gradient(180deg,#7a5a48 0%,#c99a82 30%,#f4c6b8 55%,#f6cfc4 100%);border-radius:90px 90px 0 0;opacity:.9}

/* section titles */
.section-title{left:0;width:1200px;text-align:center;font-family:'Raleway',sans-serif;font-weight:700;font-size:16px;letter-spacing:1px;color:var(--teal-dark)}
.title-rule{height:1px;background:var(--line)}

/* product card */
.card{width:194px;height:272px;background:#fff;border:2px solid #eeeeee}
.card .ph{position:absolute;left:10px;top:10px;width:170px;height:168px}
.card .name{position:absolute;left:0;right:0;top:188px;text-align:center;font-size:10.5px;letter-spacing:.5px;color:#555}
.card .price{position:absolute;left:0;right:0;top:205px;text-align:center;font-size:12px;font-weight:700;color:#444}
.card .price sup{font-size:7px}
.card .btn{position:absolute;left:60px;top:234px;width:72px;height:22px;background:var(--pink);color:#fff;font-size:9px;text-align:center;line-height:22px}
.badge{position:absolute;left:0;top:10px;width:42px;height:22px;background:#ec4a4e;color:#fff;font-size:10px;text-align:center;line-height:22px}
.ph-brick{background:linear-gradient(90deg,#b5644c 0%,#c87a60 35%,#e9c24a 50%,#c87a60 65%,#a95a44 100%)}
.ph-wood{background:linear-gradient(90deg,#9d988f 0%,#d8d4cc 35%,#5fc9c0 50%,#d8d4cc 65%,#8e8a84 100%)}
.ph-room{background:linear-gradient(180deg,#e8e4dc 0%,#9a9186 45%,#4a3f36 100%)}
.ph-floral{background:radial-gradient(ellipse at 50% 55%,#e2474f 0%,#e66a70 30%,#f6f2f2 62%)}
.ph-burgundy{background:radial-gradient(ellipse at 50% 40%,#6e1f2c 0%,#8a3a46 30%,#f8f6f6 62%)}
.ph-trousers{background:radial-gradient(ellipse at 50% 55%,#e9e9ec 0%,#dcdce0 35%,#fbfbfb 65%)}

/* special offers */
.special-bg{left:0;top:972px;width:1200px;height:409px;background:var(--soft)}
.special-title{left:129px;top:1016px;font-family:'Raleway',sans-serif;font-weight:700;font-size:16px;letter-spacing:.5px;color:var(--teal-dark)}
.arrow-sq{top:1015px;width:16px;height:16px;background:var(--red-dark)}
.tabs{left:386px;top:1012px;display:flex;font-family:'Raleway',sans-serif;font-size:13px;font-weight:600;letter-spacing:.5px}
.tabs span{padding:5px 18px;background:#ececec;color:#666}
.tabs span.on{background:#fafafa;color:var(--pink)}
.promo{left:131px;top:1057px;width:223px;height:271px}
.promo .ph{position:absolute;left:0;top:0;width:223px;height:196px}
.promo .sale{position:absolute;left:0;top:196px;width:223px;height:38px;background:var(--teal);color:#fff;font-family:'Raleway',sans-serif}
.promo .sale b{position:absolute;left:30px;top:2px;font-size:28px;font-weight:500}
.promo .sale i{position:absolute;left:102px;top:5px;font-style:normal;font-size:11px;line-height:13px}
.promo .sale em{font-style:normal;color:#ffe066;font-size:14px}
.promo .shop{position:absolute;left:0;top:234px;width:223px;height:37px;background:#ef4e5a;color:#fff;font-family:'Raleway',sans-serif;font-size:19px;text-align:center;line-height:37px}

/* brands */
.brands{left:133px;width:910px;top:1504px;display:flex;justify-content:space-between;align-items:center}
.brands span{font-family:'Raleway',sans-serif;font-weight:800;font-size:19px;letter-spacing:.5px;color:#222}
.brands span.mark{display:flex;align-items:center;gap:7px}
.brands span.mark i{display:inline-block;width:12px;height:12px;background:var(--red)}

/* offer band */
.band{left:0;top:1607px;width:1200px;height:229px;background:var(--pink-band)}
.band-photo{left:130px;top:1607px;width:230px;height:229px;background:linear-gradient(90deg,rgba(255,138,140,0),#e63c3c 25%,#d62a2a 65%,rgba(255,138,140,0))}
.band-text{left:330px;top:1668px;width:400px;text-align:right;font-family:'Raleway',sans-serif;font-size:22px;line-height:30px;color:#fff}
.band-off{left:754px;top:1650px;font-family:'Raleway',sans-serif;font-weight:800;font-size:72px;line-height:80px;color:#fff}
.band-off span{color:var(--red)}
.band-btn{top:1750px;height:40px;font-family:'Raleway',sans-serif;font-weight:700;font-size:14px;letter-spacing:1px;text-align:center;line-height:40px}

/* newsletter */
.notify{left:140px;top:1917px;font-style:italic;font-size:18px;color:#666}
.email{left:457px;top:1902px;width:485px;height:54px;border:1px solid #ddd;font-size:14px;color:#999;padding:17px 16px}
.go{left:960px;top:1902px;width:100px;height:54px;background:#c9454f;color:#fff;font-size:19px;text-align:center;line-height:54px}

/* footer */
.footer{left:0;top:2031px;width:1200px;height:324px;background:#fafafa;border-top:1px solid #eee}
.f-head{top:2076px;font-size:15px;color:#333}
.f-text{font-size:11px;line-height:19px;color:#777}
.f-link{font-size:11px;line-height:24px;color:#888}
.post-t{font-size:12px;font-weight:700;color:#444}
.post-t.hot{color:var(--red)}
.tweet{left:805px;top:2124px;width:233px;height:100px;background:#fff;border:1px solid #eee;font-style:italic;font-size:10px;line-height:15px;color:#666;text-align:center;padding:10px 16px}
.copy-bar{left:0;top:2355px;width:1200px;height:48px;background:#fff;border-top:1px solid #e6e6e6}
.copy{left:138px;top:2372px;font-size:10.5px;color:#999}
.pay{top:2370px;height:18px;width:26px;border:1px solid #ccc;font-size:6.5px;color:#666;text-align:center;line-height:16px}
</style>
</head>
<body>

<!-- header -->
<div class="abs social-top"><span>Fenlo</span><span>Chirra</span><span>Rsfeed</span></div>
<div class="abs brand">TrelWick</div>
<div class="abs user">Howdy Mara Loen &nbsp;|&nbsp; <b>Logout</b></div>
<div class="abs cart">
  <svg width="34" height="35" viewBox="0 0 34 35"><path d="M9 11h3l2 9h9l2-7H13" fill="none" stroke="#777" stroke-width="1.6"/><circle cx="15" cy="23" r="1.4" fill="#777"/><circle cx="22" cy="23" r="1.4" fill="#777"/></svg>
</div>
<div class="abs cart-count">3</div>
<div class="abs search">Search
  <svg class="abs" style="right:8px;top:9px" width="14" height="14" viewBox="0 0 14 14"><circle cx="6" cy="6" r="4.5" fill="none" stroke="#888" stroke-width="1.6"/><path d="M9.5 9.5l3.5 3.5" stroke="#888" stroke-width="1.8"/></svg>
</div>
<nav class="abs nav">
  <a class="active">Home</a><a>Women</a><a>Men</a><a>Shop now</a><a>About</a><a>Blog</a><a>Support</a>
</nav>
<div class="abs nav-rule"></div>
<div class="abs nav-dot" style="left:486px"></div>
<div class="abs nav-dot" style="left:536px"></div>
<div class="abs nav-dot" style="left:576px"></div>
<div class="abs nav-dot" style="left:616px"></div>
<div class="abs nav-dot" style="left:665px"></div>

<!-- hero -->
<section class="abs hero"></section>
<div class="abs hero-photo" role="img" aria-label="Model with long wavy hair in a blush pink lace top"></div>
<svg class="abs" style="left:158px;top:328px" width="22" height="42" viewBox="0 0 22 42"><path d="M20 2L3 21l17 19" fill="none" stroke="#fff" stroke-width="1.5" opacity=".8"/></svg>
<svg class="abs" style="left:998px;top:328px" width="22" height="42" viewBox="0 0 22 42"><path d="M2 2l17 19L2 40" fill="none" stroke="#fff" stroke-width="1.5" opacity=".8"/></svg>
<h1 class="abs hero-title">NEW SEASON ARRIVALS.</h1>
<p class="abs hero-sub">CHECK OUT ALL THE NEW TRENDS</p>
<div class="abs hero-btn">SHOP NOW</div>

<!-- latest products -->
<div class="abs title-rule" style="left:372px;top:594px;width:456px"></div>
<h2 class="abs section-title" style="top:584px"><span style="background:#fff;padding:0 16px">LATEST PRODUCTS</span></h2>

<div class="abs card" style="left:131px;top:644px">
  <div class="ph ph-brick" role="img" aria-label="Model in red top and yellow skirt by a brick wall"></div>
  <div class="badge">-86%</div>
  <div class="name">DOLORE EU NULLA PARIATUR.</div><div class="price">$120<sup>.00</sup></div><div class="btn">SHOP NOW</div>
</div>
<div class="abs card" style="left:380px;top:644px">
  <div class="ph ph-wood" role="img" aria-label="Model in teal cardigan and striped skirt by weathered wood"></div>
  <div class="name">ENIM AD MINIM VENIAM.</div><div class="price">$1000<sup>.00</sup></div><div class="btn">SHOP NOW</div>
</div>
<div class="abs card" style="left:621px;top:644px">
  <div class="ph ph-room" role="img" aria-label="Model seated on a suitcase by a window"></div>
  <div class="name">EXCEPTEUR SINT CUPIDATAT.</div><div class="price">$340<sup>.00</sup></div><div class="btn">SHOP NOW</div>
</div>
<div class="abs card" style="left:873px;top:644px">
  <div class="ph ph-brick" role="img" aria-label="Model in red top and yellow skirt by a brick wall"></div>
  <div class="badge">-86%</div>
  <div class="name">DOLORE EU NULLA PARIATUR.</div><div class="price">$120<sup>.00</sup></div><div class="btn">SHOP NOW</div>
</div>

<!-- special offers -->
<section class="abs special-bg"></section>
<h2 class="abs special-title">SPECIAL OFFERS</h2>
<div class="abs arrow-sq" style="left:311px"><svg width="16" height="16"><path d="M10 4L6 8l4 4" fill="none" stroke="#fff" stroke-width="1.6"/></svg></div>
<div class="abs arrow-sq" style="left:334px"><svg width="16" height="16"><path d="M6 4l4 4-4 4" fill="none" stroke="#fff" stroke-width="1.6"/></svg></div>
<div class="abs tabs"><span>HIGH RATED</span><span class="on">HOT DEALS</span><span>BEST SELLER</span></div>

<div class="abs promo">
  <div class="ph ph-wood" role="img" aria-label="Model in teal cardigan and striped skirt by weathered wood"></div>
  <div class="sale"><b>SALE</b><i>up to <em>60%</em> off<br>to all TOPS</i></div>
  <div class="shop">SHOP NOW</div>
</div>
<div class="abs card" style="left:386px;top:1057px;height:271px">
  <div class="ph ph-floral" role="img" aria-label="Model in red floral short-sleeve top"></div>
  <div class="badge">-86%</div>
  <div class="name">DOLORE EU NULLA PARIATUR.</div><div class="price">$120<sup>.00</sup></div><div class="btn">SHOP NOW</div>
</div>
<div class="abs card" style="left:631px;top:1057px;height:271px">
  <div class="ph ph-burgundy" role="img" aria-label="Model in burgundy blouse and white trousers"></div>
  <div class="name">ENIM AD MINIM VENIAM.</div><div class="price">$1000<sup>.00</sup></div><div class="btn">SHOP NOW</div>
</div>
<div class="abs card" style="left:874px;top:1057px;height:271px">
  <div class="ph ph-trousers" role="img" aria-label="White trousers with red belt"></div>
  <div class="name">EXCEPTEUR SINT CUPIDATAT.</div><div class="price">$340<sup>.00</sup></div><div class="btn">SHOP NOW</div>
</div>

<!-- top brands -->
<div class="abs title-rule" style="left:440px;top:1437px;width:320px"></div>
<h2 class="abs section-title" style="top:1427px"><span style="background:#fff;padding:0 16px">TOP BRANDS</span></h2>
<div class="abs brands">
  <span>NORVANE</span>
  <span>CRESMONT</span>
  <span class="mark"><i></i>HALVIK</span>
  <span>NORVANE</span>
  <span>ORLENE</span>
  <span class="mark"><i></i>HALVIK</span>
  <span>ORLENE</span>
</div>

<!-- offer band -->
<section class="abs band"></section>
<div class="abs band-photo" role="img" aria-label="Model in red sheer-yoke blouse"></div>
<p class="abs band-text">LOREM IPSUM IS SIMPLY DUMMY<br>TEXT OF THE PRINTING</p>
<div class="abs band-off">20%<span>OFF</span></div>
<div class="abs band-btn" style="left:551px;width:170px;background:#fff;color:var(--teal-dark)">SHOP NOW</div>
<div class="abs band-btn" style="left:744px;width:170px;background:var(--red);color:#fff">MORE OFFER</div>

<!-- newsletter -->
<p class="abs notify">Notify me when new product arrives</p>
<div class="abs email">Enter your mail address</div>
<div class="abs go">GO</div>

<!-- footer -->
<footer class="abs footer"></footer>
<h3 class="abs f-head" style="left:144px;font-weight:700">Our Stores</h3>
<div class="abs f-text" style="left:144px;top:2117px">0188 Brindle Court<br>Larkfield, CA 15400<br><b style="color:#555">(555) 014-2290</b></div>
<div class="abs f-text" style="left:144px;top:2197px">42 Ashmoor Lane<br>Tennant, VA 23800<br><b style="color:#555">(555) 017-3344</b></div>
<div class="abs" style="left:144px;top:2285px;display:flex;gap:12px;font-size:9px;color:#2c4a78">
  <span>Fenlo</span><span>Chirra</span><span>Gplo</span><span>Vidra</span><span>Rss</span>
</div>

<h3 class="abs f-head" style="left:349px;font-weight:700">Blog Posts</h3>
<div class="abs" style="left:349px;top:2117px;width:240px">
  <p class="post-t hot">Duis aute irure dolor in reprehenderit.</p>
  <p class="f-text" style="line-height:16px;margin-bottom:12px">in voluptate velit esse cillum dolore eu fugiat nulla pariatur.</p>
  <p class="post-t">Ut enim ad minim veniam.</p>
  <p class="f-text" style="line-height:16px;margin-bottom:12px">in voluptate velit esse cillum dolore eu fugiat nulla pariatur.</p>
  <p class="post-t">officia deserunt mollit consectetur.</p>
  <p class="f-text" style="line-height:16px">in voluptate velit esse cillum dolore eu fugiat nulla pariatur.</p>
</div>

<h3 class="abs f-head" style="left:666px;font-weight:700">Support</h3>
<div class="abs f-link" style="left:666px;top:2114px">Terms &amp; Conditions<br>FAQ<br>Payment<br>Returns<br>Track Order<br>Services</div>

<svg class="abs" style="left:803px;top:2079px" width="16" height="14" viewBox="0 0 16 14"><path d="M2 3l6 4 6-4v8H2z" fill="none" stroke="#4aa8e0" stroke-width="1.4"/></svg>
<h3 class="abs f-head" style="left:830px;top:2078px;font-weight:700">Latest tweets</h3>
<div class="abs tweet">Lorem ipsum dolor sit amet, consectetur adipiscing elit. Sed ut tellus ac nulla semper rhoncus. Nullam a odio porttitor, dictum turpis vitae, pretium ante amet.</div>
<div class="abs" style="left:810px;top:2230px;font-size:8px;font-weight:700;color:#444">Kestry Daily <span style="font-weight:400">@kestry</span></div>
<div class="abs" style="left:898px;top:2262px;display:flex;gap:6px">
  <i style="width:8px;height:8px;border-radius:50%;background:#bbb"></i>
  <i style="width:8px;height:8px;border-radius:50%;border:1px solid #ccc"></i>
  <i style="width:8px;height:8px;border-radius:50%;border:1px solid #ccc"></i>
</div>

<div class="abs copy-bar"></div>
<p class="abs copy">© 2014trelwick.com &nbsp;- &nbsp;All Rights Reserved</p>
<div class="abs pay" style="left:950px">Pavo</div>
<div class="abs pay" style="left:982px">Mercel</div>
<div class="abs pay" style="left:1014px">Dovin</div>
<div class="abs pay" style="left:1046px;width:20px">Amb</div>

</body>
</html>
```